依頼詳細
シンプルなデザイン(白・黒)を基調としたデザインをお願いたします。
洗練された雰囲気のあるデザインが希望です。

縦・横それぞれ候補頂けますと幸いです。
記載項目
表面
株式会社ルカ
東京都柊野町14-57-215
TEL:03-5872-1946
FAX:03-5872-1953
HANDY:080-7259-8421
Mail:tani@ruka-example.jp

裏面
ロゴ+何か(会社HPに飛ぶHPでもいいです)
※ロゴだけでもカッコよければそれでもいいかと思ってます。
希望イメージ
希望する色
無彩色系
納品ファイル
• 高解像度JPG (.jpg)
補足説明
従来の縦型のデザインを送ります。
裏面は黒バックにロゴのみでした。

デザインが気に入りました。

この度は、お忙しい中ご提案頂きまして誠にありがとうございました。
また何かありましたら、お付き合いの程よろしくお願い申し上げます。

```html
<!DOCTYPE html>
<html lang="ja">
<head>
<meta charset="utf-8">
<title>株式会社ルカ 名刺</title>
<link href="https://fonts.googleapis.com/css2?family=Noto+Sans+JP:wght@300;400&display=swap" rel="stylesheet">
<style>
  :root {
    --ink: #2c2a55;
    --light-core: #ffffff;
    --light-mid: #ece9ec;
    --light-edge: #b9b4b8;
    --shadow-edge: #8f898e;
  }
  html, body {
    margin: 0;
    padding: 0;
    width: 755px;
    height: 1200px;
    overflow: hidden;
    background: #ffffff;
  }
  .card {
    position: relative;
    width: 755px;
    height: 1200px;
    overflow: hidden;
    font-family: "Noto Sans JP", sans-serif;
    color: var(--ink);
  }
  .card__backdrop {
    position: absolute;
    inset: 0;
    background:
      radial-gradient(ellipse 38% 26% at 50% 46%, var(--light-core) 0%, rgba(255,255,255,0.85) 40%, rgba(255,255,255,0) 100%),
      radial-gradient(ellipse 80% 60% at 50% 48%, var(--light-mid) 0%, var(--light-edge) 75%, var(--shadow-edge) 100%);
  }
  .company-name {
    position: absolute;
    top: 572px;
    left: 0;
    width: 100%;
    margin: 0;
    text-align: center;
    font-size: 42px;
    font-weight: 400;
    letter-spacing: 0.02em;
  }
  .contact {
    position: absolute;
    left: 90px;
    top: 798px;
    margin: 0;
    padding: 0;
    list-style: none;
    font-size: 35px;
    font-weight: 300;
    line-height: 57px;
    letter-spacing: 0.01em;
  }
  .contact__line { white-space: nowrap; }
</style>
</head>
<body>
  <div class="card">
    <div class="card__backdrop" role="img" aria-label="白く光る回廊と中央に浮かぶ透明な立方体の写真"></div>
    <h1 class="company-name">株式会社ルカ</h1>
    <ul class="contact">
      <li class="contact__line">東京都柊野町14-57-215</li>
      <li class="contact__line">TEL:03-5872-1946</li>
      <li class="contact__line">FAX:03-5872-1953</li>
      <li class="contact__line">HANDY:080-7259-8421</li>
      <li class="contact__line">Mail:tani@ruka-example.jp</li>
    </ul>
  </div>
</body>
</html>
```